Bright Loom Allies, LLC
Collaborative Contract Solutions
Modern
Owen Darby
Managing Director
12 Juniper Vale Road
Suite 240
Danvers, MA 01847
owen@brightloomallies.com
www.brightloomallies.com
Docs said to upload this logo format.

```html
<!DOCTYPE html>
<html lang="en">
<head>
<meta charset="utf-8">
<title>Bright Loom Allies, LLC — Stationery</title>
<link href="https://fonts.googleapis.com/css2?family=Open+Sans:wght@400;600;700&display=swap" rel="stylesheet">
<style>
  :root {
    --blue: #1d93d8;
    --blue-deep: #0e62a6;
    --blue-soft: #c9e6f7;
    --ink: #3c4650;
    --muted: #7b8791;
    --paper: #ffffff;
    --stage: #e6e8eb;
  }
  * { margin: 0; padding: 0; box-sizing: border-box; }
  html, body { width: 1200px; height: 674px; overflow: hidden; }
  body {
    background: var(--stage);
    font-family: "Open Sans", Arial, sans-serif;
    color: var(--ink);
    position: relative;
  }
  .sheet {
    position: absolute;
    background: var(--paper);
    box-shadow: 0 2px 6px rgba(0,0,0,.18);
    overflow: hidden;
  }
  .brand {
    display: flex; align-items: center; gap: 5px;
    color: var(--blue-deep); font-weight: 700; white-space: nowrap;
  }
  .brand .dot { border-radius: 50%; background: var(--blue); flex: none; }
  .band {
    position: absolute; left: 0; right: 0; bottom: 0;
    background: linear-gradient(180deg, var(--blue) 0%, var(--blue-deep) 100%);
  }
  .band svg { position: absolute; left: 0; top: -10px; width: 100%; height: 12px; }
  .floral {
    position: absolute; border-radius: 50%;
    background: radial-gradient(circle, rgba(29,147,216,.14) 0%, rgba(29,147,216,.05) 55%, rgba(29,147,216,0) 72%);
  }

  /* business cards */
  .card { left: 34px; width: 163px; height: 104px; }
  .card-front { top: 19px; }
  .card-front .brand { position: absolute; left: 14px; top: 36px; font-size: 11px; }
  .card-front .brand .dot { width: 10px; height: 10px; }
  .card-front .person { position: absolute; right: 10px; top: 8px; text-align: right; font-size: 5px; color: var(--muted); line-height: 1.4; }
  .card-front .person b { display: block; font-size: 6px; color: var(--ink); }
  .card-front .band { height: 30px; color: #fff; font-size: 4.6px; line-height: 1.5; padding: 7px 12px 0; }

  .card-web { top: 192px; }
  .card-web .brand { position: absolute; left: 14px; top: 26px; font-size: 10px; }
  .card-web .brand .dot { width: 9px; height: 9px; }
  .card-web .band { height: 30px; color: #fff; font-size: 5.4px; padding: 11px 0 0; text-align: center; }

  .card-back { top: 302px; background: linear-gradient(160deg, var(--blue) 0%, var(--blue-deep) 100%); color: #fff; }
  .card-back .floral { width: 120px; height: 120px; right: -30px; top: -20px; background: radial-gradient(circle, rgba(255,255,255,.22) 0%, rgba(255,255,255,.06) 55%, rgba(255,255,255,0) 72%); }
  .card-back .person { position: absolute; left: 12px; top: 12px; font-size: 5px; line-height: 1.4; }
  .card-back .person b { display: block; font-size: 6px; }
  .card-back .contact { position: absolute; left: 12px; bottom: 12px; font-size: 4.6px; line-height: 1.5; }

  /* letterhead */
  .letterhead { left: 233px; top: 19px; width: 281px; height: 629px; }
  .letterhead .floral { width: 240px; height: 240px; right: -120px; top: 300px; }
  .letterhead .brand { position: absolute; left: 0; right: 0; top: 38px; justify-content: center; font-size: 13px; }
  .letterhead .brand .dot { width: 11px; height: 11px; }
  .letter { position: absolute; left: 24px; right: 24px; top: 100px; font-size: 4.8px; line-height: 1.6; }
  .letter p { margin-bottom: 8px; }
  .letter .recipient { margin-bottom: 14px; }
  .letter .signoff { text-align: right; margin-top: 40px; }
  .letterhead .band { height: 36px; color: #fff; font-size: 4.6px; line-height: 1.6; text-align: center; padding-top: 11px; }

  /* envelope */
  .envelope-front { left: 538px; top: 331px; width: 633px; height: 149px; }
  .envelope-front .floral { width: 300px; height: 300px; left: 290px; top: -150px; }
  .envelope-front .brand { position: absolute; left: 30px; top: 34px; font-size: 14px; }
  .envelope-front .brand .dot { width: 12px; height: 12px; }
  .envelope-front .return { position: absolute; left: 30px; top: 60px; font-size: 4.8px; color: var(--muted); }
  .envelope-front .band { height: 26px; }

  .envelope-back { left: 538px; top: 485px; width: 633px; height: 158px; }
  .envelope-back svg.flap { position: absolute; left: 0; top: 0; width: 100%; height: 100%; }
</style>
</head>
<body>

  <section class="sheet card card-front" aria-label="Business card front">
    <div class="person"><b>Owen Darby</b>Managing Director</div>
    <div class="brand"><span class="dot"></span>Bright Loom Allies</div>
    <div class="band">
      <svg viewBox="0 0 163 12" preserveAspectRatio="none"><path d="M0 12 Q80 0 163 8 L163 12 Z" fill="#1d93d8"/></svg>
      12 Juniper Vale Road, Suite 240, Danvers, MA 01847<br>
      T: 978-555-0142 &nbsp;|&nbsp; owen@brightloomallies.com
    </div>
  </section>

  <section class="sheet card card-web" aria-label="Business card web side">
    <div class="brand"><span class="dot"></span>Bright Loom Allies</div>
    <div class="band">
      <svg viewBox="0 0 163 12" preserveAspectRatio="none"><path d="M0 12 Q80 0 163 8 L163 12 Z" fill="#1d93d8"/></svg>
      www.brightloomallies.com
    </div>
  </section>

  <section class="sheet card card-back" aria-label="Business card back">
    <div class="floral" role="img" aria-label="faint floral pattern"></div>
    <div class="person"><b>Owen Darby</b>Managing Director</div>
    <div class="contact">
      12 Juniper Vale Road, Suite 240<br>
      Danvers, MA 01847<br>
      T: 978-555-0142<br>
      owen@brightloomallies.com
    </div>
  </section>

  <section class="sheet letterhead" aria-label="Letterhead">
    <div class="floral" role="img" aria-label="faint floral pattern"></div>
    <div class="brand"><span class="dot"></span>Bright Loom Allies</div>
    <div class="letter">
      <p class="recipient">To<br>Mr. Alan Reed<br>Managing Director</p>
      <p>Sir,</p>
      <p>Thank you for meeting with our team last week. We appreciate the time you gave to review our proposal and the clear notes you shared on scope, budget and timing. Our partners have revised the plan to reflect each point, and the updated contract terms are enclosed for your review.</p>
      <p>We are confident this shared approach will give your staff the support they need while keeping costs steady. Please let us know if you would like to schedule a follow-up call.</p>
      <p class="signoff">Sincerely,<br>Owen Darby<br>Managing Director</p>
    </div>
    <div class="band">
      <svg viewBox="0 0 281 12" preserveAspectRatio="none"><path d="M0 12 Q140 0 281 8 L281 12 Z" fill="#1d93d8"/></svg>
      12 Juniper Vale Road, Suite 240, Danvers, MA 01847<br>
      T: 978-555-0142 &nbsp;|&nbsp; E: owen@brightloomallies.com &nbsp;|&nbsp; W: www.brightloomallies.com
    </div>
  </section>

  <section class="sheet envelope-front" aria-label="Envelope front">
    <div class="floral" role="img" aria-label="faint floral pattern"></div>
    <div class="brand"><span class="dot"></span>Bright Loom Allies</div>
    <div class="return">12 Juniper Vale Road, Suite 240, Danvers, MA 01847 &nbsp;|&nbsp; T: 978-555-0142 &nbsp;|&nbsp; owen@brightloomallies.com &nbsp;|&nbsp; www.brightloomallies.com</div>
    <div class="band">
      <svg viewBox="0 0 633 12" preserveAspectRatio="none"><path d="M0 12 Q320 0 633 8 L633 12 Z" fill="#1d93d8"/></svg>
    </div>
  </section>

  <section class="sheet envelope-back" aria-label="Envelope back">
    <svg class="flap" viewBox="0 0 633 158" preserveAspectRatio="none">
      <defs>
        <linearGradient id="flap-blue" x1="0" y1="0" x2="0" y2="1">
          <stop offset="0" stop-color="#1d93d8"/>
          <stop offset="1" stop-color="#0e62a6"/>
        </linearGradient>
      </defs>
      <path d="M0 0 L633 0 L633 30 L330 92 Q316 95 302 92 L0 30 Z" fill="#f7f9fb" stroke="#dfe4e8" stroke-width="1"/>
      <path d="M0 158 L0 120 Q316 95 633 120 L633 158 Z" fill="url(#flap-blue)"/>
      <path d="M0 30 L302 92 Q316 95 330 92 L633 30" fill="none" stroke="#d5dbe0" stroke-width="1"/>
    </svg>
  </section>

</body>
</html>
```